Adult Literacy Program - flyer to attract volunteers and students

We want a flyer that is engaging, colorful, modern and will appeal to our primary audience of adults aged 40-60. We are trying to attract both prospective volunteers (typically age 50+, mostly women) and students (typically aged 40+).
The flyer should feature diverse people working together in pairs of two, reading or talking, with a workbook or some reading material in front of them.

Our organization trains tutors to work one-on-one with adults who are learning how to read. Most of our adult students are non-native speakers of English. Many are of Haitian or Hispanic origin, so we would like some people who represent that demographic.

The Flyer should represent reading, learning, literacy, knowledge, growth,
and opportunities.
Our students are learning to read so they can advance their job opportunities.

Target Market(s)

Adults aged 40-60, primarily women, retired, volunteers

Industry/Entity Type

Education

Font styles to use
Serif
Sans Serif

Colors

Designer to choose colors to be used in the design.

Requirements
Must have
• - UPDATE: Should be designed as a TRI-FOLD brochure on 8.5 x 11 inch paper that will be folded into thirds.
• - Images of diverse people, women and men, who look Hispanic, Haitian and other nationalities as well as Caucasian.
• - Our logo on the front cover
Nice to have
• The sample flyer is very boring and dry! We are open to different ways of presenting the text.

```html
<!DOCTYPE html>
<html lang="en">
<head>
<meta charset="utf-8">
<title>Reading Bridge Partners – Volunteer Tri-fold</title>
<link href="https://fonts.googleapis.com/css2?family=Lato:wght@400;700;900&display=swap" rel="stylesheet">
<style>
  :root{
    --navy:#1b2a6b;
    --blue:#1c9bd8;
    --sky:#40c2ef;
    --white:#ffffff;
    --stage:#ececec;
  }
  html,body{margin:0;padding:0;overflow:hidden;}
  body{background:var(--stage);font-family:"Lato",Arial,sans-serif;}
  .canvas{position:relative;width:895px;height:1200px;overflow:hidden;background:var(--stage);}
  .sheet{position:absolute;left:30px;width:835px;height:545px;overflow:hidden;
         box-shadow:0 4px 14px rgba(0,0,0,.18);}
  .sheet--outside{top:40px;}
  .sheet--inside{top:615px;}
  .sheet svg.art{position:absolute;inset:0;width:100%;height:100%;}
  .text{position:absolute;color:var(--white);}
  .headline{color:var(--navy);font-weight:900;line-height:1;margin:0;}
  .contact{left:318px;top:52px;width:230px;text-align:center;}
  .contact .headline{font-size:29px;}
  .contact .lead{font-weight:900;font-size:18px;line-height:1.05;margin:12px 0 16px;}
  .contact p{margin:0 0 10px;font-size:13px;line-height:1.25;}
  .contact strong{font-size:17px;font-weight:900;}
  .contact .big{font-size:21px;}
  .contact .email{font-weight:700;font-size:13px;}
  .brand{position:absolute;display:flex;align-items:center;justify-content:center;text-align:center;
         color:var(--navy);font-weight:900;font-size:11px;line-height:1.15;letter-spacing:.5px;}
  .brand--tab{left:628px;top:24px;width:96px;height:56px;}
  .brand--seal-out{left:382px;top:425px;width:82px;height:56px;}
  .brand--seal-in{left:377px;top:215px;width:82px;height:56px;}
  .cover{left:560px;top:112px;width:260px;}
  .cover .headline{font-size:40px;letter-spacing:.5px;}
  .pill{display:inline-block;background:var(--navy);color:var(--white);font-size:15px;
        padding:4px 14px;border-radius:14px 0 0 14px;margin:6px 0 0 100px;}
  .cover p{font-size:14px;line-height:1.25;margin:14px 0 0 20px;}
  .tutors{left:30px;top:150px;width:290px;}
  .section-title{color:var(--navy);font-weight:900;font-size:25px;margin:0 0 8px;}
  .list{margin:0;padding-left:18px;font-size:12.5px;line-height:1.35;}
  .tagline{left:30px;top:372px;width:250px;color:var(--navy);font-weight:900;font-size:24px;line-height:1.08;}
  .students{left:598px;top:30px;width:225px;}
  .students .section-title{font-size:21px;margin-bottom:4px;}
  .students .list{font-size:11px;}
  .students .list ul{padding-left:14px;margin:0;}
  .students .callout{color:var(--navy);font-weight:900;font-size:18px;text-align:center;line-height:1.1;margin-top:14px;}
</style>
</head>
<body>
<div class="canvas">

  <section class="sheet sheet--outside">
    <svg class="art" viewBox="0 0 835 545" xmlns="http://www.w3.org/2000/svg">
      <defs>
        <linearGradient id="bgOut" x1="0" y1="0" x2="1" y2="1">
          <stop offset="0" stop-color="#2fb6ea"/><stop offset="1" stop-color="#1787c9"/>
        </linearGradient>
        <linearGradient id="photoWarm" x1="0" y1="0" x2="1" y2="1">
          <stop offset="0" stop-color="#3a3f4a"/><stop offset=".5" stop-color="#b9a898"/><stop offset="1" stop-color="#2e7fa3"/>
        </linearGradient>
        <linearGradient id="photoShelf" x1="0" y1="0" x2="1" y2="1">
          <stop offset="0" stop-color="#a24a44"/><stop offset=".5" stop-color="#d9cbb8"/><stop offset="1" stop-color="#e9e3d6"/>
        </linearGradient>
      </defs>
      <rect width="835" height="545" fill="url(#bgOut)"/>
      <path d="M0,0 H300 C285,120 340,200 300,300 C270,380 300,470 330,545 H0 Z" fill="var(--navy)"/>
      <path role="img" aria-label="Photo: a volunteer tutor and an adult learner smiling together over an open workbook" d="M0,0 H288 C273,120 328,200 288,300 C258,380 288,470 318,545 H0 Z" fill="url(#photoWarm)"/>
      <path d="M835,210 C780,240 720,250 700,285 L835,285 Z" fill="var(--navy)"/>
      <path d="M525,545 C525,400 600,300 700,285 C760,275 800,260 835,245 V545 Z" fill="var(--navy)"/>
      <path role="img" aria-label="Photo: an older woman reading a book in front of library shelves" d="M540,545 C540,410 610,312 705,298 C765,289 805,275 835,260 V545 Z" fill="url(#photoShelf)"/>
      <path d="M605,0 H748 V75 C748,105 720,118 676,118 C632,118 605,105 605,75 Z" fill="var(--navy)"/>
      <path d="M612,0 H741 V72 C741,100 715,110 676,110 C637,110 612,100 612,72 Z" fill="var(--white)"/>
      <circle cx="423" cy="453" r="52" fill="var(--navy)"/>
      <circle cx="423" cy="453" r="46" fill="var(--white)"/>
    </svg>

    <div class="text contact">
      <h2 class="headline">Don't waste a moment!</h2>
      <div class="lead">Contact us today<br>to learn more.</div>
      <p>Volunteer Desk: <strong>555-201-4410</strong></p>
      <p>Lakeview, Pine Ridge &amp; East Harbor: <strong class="big">555-207-3318</strong></p>
      <p class="email">email: tutors@readingbridge.org</p>
    </div>

    <div class="brand brand--tab">READING BRIDGE PARTNERS</div>
    <div class="brand brand--seal-out">READING BRIDGE PARTNERS</div>

    <div class="text cover">
      <h1 class="headline">VOLUNTEER</h1>
      <span class="pill">Enrich a Life!</span>
      <p>Help an adult learn to read,<br>write or speak English</p>
    </div>
  </section>

  <section class="sheet sheet--inside">
    <svg class="art" viewBox="0 0 835 545" xmlns="http://www.w3.org/2000/svg">
      <defs>
        <linearGradient id="bgIn" x1="0" y1="0" x2="1" y2="1">
          <stop offset="0" stop-color="#2fb6ea"/><stop offset="1" stop-color="#1a8fd0"/>
        </linearGradient>
        <linearGradient id="photoPair" x1="0" y1="0" x2="1" y2="0">
          <stop offset="0" stop-color="#3b4152"/><stop offset=".45" stop-color="#c8b9aa"/><stop offset="1" stop-color="#4e4a48"/>
        </linearGradient>
        <linearGradient id="photoGroup" x1="0" y1="0" x2="1" y2="1">
          <stop offset="0" stop-color="#8a6d58"/><stop offset=".5" stop-color="#e4ddd2"/><stop offset="1" stop-color="#a9c3dc"/>
        </linearGradient>
      </defs>
      <rect width="835" height="545" fill="url(#bgIn)"/>
      <path d="M0,0 H600 C575,130 490,215 400,220 C250,228 120,135 0,125 Z" fill="var(--navy)"/>
      <path role="img" aria-label="Photo: a woman and a man studying together at a library table" d="M0,0 H585 C560,122 480,203 400,208 C250,215 120,125 0,113 Z" fill="url(#photoPair)"/>
      <path d="M235,545 C290,395 400,310 560,290 C690,275 765,255 835,225 V545 Z" fill="var(--navy)"/>
      <path role="img" aria-label="Photo: a smiling woman at a study table with adult learners working in pairs behind her" d="M252,545 C305,405 410,323 562,303 C690,288 765,268 835,240 V545 Z" fill="url(#photoGroup)"/>
      <circle cx="418" cy="243" r="54" fill="var(--navy)"/>
      <circle cx="418" cy="243" r="48" fill="var(--white)"/>
    </svg>

    <div class="text tutors">
      <h2 class="section-title">Tutors</h2>
      <ul class="list">
        <li>No special skills or degrees needed — just a degree of caring!</li>
        <li>Training offered throughout the year</li>
        <li>Tutors meet students weekly at a library</li>
        <li>Instructional materials provided</li>
        <li>Ongoing support available</li>
      </ul>
    </div>
    <div class="text tagline">Teach an adult to read and you'll change a life forever.</div>

    <div class="brand brand--seal-in">READING BRIDGE PARTNERS</div>

    <div class="text students">
      <h2 class="section-title">Students</h2>
      <ul class="list">
        <li>Students are adults in need of
          <ul><li>basic literacy skills</li><li>pre-GED skills</li><li>conversational English</li></ul>
        </li>
        <li>Tutoring is free of charge</li>
        <li>Tutoring is one-on-one</li>
        <li>Flexible scheduling during library hours</li>
        <li>Lessons focus on student goals</li>
      </ul>
      <div class="callout">If you can read, you can tutor!</div>
    </div>
  </section>

</div>
</body>
</html>
```